Sign listing benefits of Wash and Fold Service

Sign 48 inches wide and 24 inches height to showcase service listed above.
Benefits include:
Saves Money
Saves Time
Convenient
Stain Treatment

Looking for something colorful (Blue and white are our business colors) the look of a laundromat business.

```html
<!DOCTYPE html>
<html lang="en">
<head>
<meta charset="utf-8">
<title>Wash &amp; Fold Service Sign</title>
<link href="https://fonts.googleapis.com/css2?family=Alfa+Slab+One&family=Poppins:wght@600;700&display=swap" rel="stylesheet">
<style>
  :root {
    --page: #ffffff;
    --navy: #0d2f86;
    --blue: #1f6be0;
    --orange: #f7941d;
    --ink: #17181c;
    --sky-light: #e3f3fd;
    --sky: #8fd0f3;
    --sky-deep: #3ea6e4;
  }
  * { margin: 0; padding: 0; box-sizing: border-box; }
  html, body { width: 834px; height: 1200px; overflow: hidden; background: var(--page); }
  .sign {
    position: absolute; left: 27px; top: 405px;
    width: 780px; height: 390px; overflow: hidden;
    background: linear-gradient(100deg, #ffffff 0%, #ffffff 38%, var(--sky-light) 55%, var(--sky) 80%, var(--sky-deep) 100%);
    box-shadow: 0 1px 4px rgba(0,0,0,.25);
  }
  .sign__footer {
    position: absolute; left: 0; right: 0; top: 314px; bottom: 0; background: #ffffff;
  }
  .hero-photo {
    position: absolute; left: 535px; top: 0; width: 245px; height: 390px;
    background: linear-gradient(180deg, rgba(143,208,243,0) 0%, rgba(183,205,222,.55) 35%, rgba(226,196,170,.55) 70%, rgba(246,240,228,.85) 100%);
  }
  .headline {
    position: absolute; left: 31px; top: 28px; z-index: 2;
    font-family: "Alfa Slab One", Georgia, serif;
    font-size: 47px; line-height: 52px; letter-spacing: 0.5px;
  }
  .headline span { display: block; }
  .headline__lead { color: var(--blue); }
  .headline__service { color: var(--orange); }
  .headline__tail { color: var(--ink); }
  .benefits {
    position: absolute; left: 0; top: 195px; width: 521px; height: 119px; z-index: 2;
    background: var(--navy);
  }
  .benefit {
    position: absolute; display: flex; align-items: center; gap: 9px;
    font-family: "Poppins", Arial, sans-serif; font-weight: 600;
    font-size: 20px; color: #ffffff; letter-spacing: 0.2px; line-height: 1;
  }
  .benefit svg { width: 21px; height: 21px; flex: none; }
  .contact {
    position: absolute; left: 31px; top: 333px; z-index: 2;
    display: flex; align-items: center; gap: 7px;
    font-family: "Poppins", Arial, sans-serif; font-weight: 700; color: var(--ink);
  }
  .contact svg { width: 18px; height: 18px; flex: none; }
  .contact__phone { font-size: 21px; }
  .contact__divider { color: var(--blue); font-size: 20px; margin: 0 2px; font-weight: 600; }
  .contact__web { font-size: 17.5px; }
  .contact__web b { color: var(--blue); font-weight: 700; }
</style>
</head>
<body>
  <main class="sign">
    <div class="sign__footer"></div>

    <div class="hero-photo" role="img" aria-label="Photo of a smiling laundry attendant in an apron beside a wicker basket of folded towels, colourful laundry and daisies, in front of soap bubbles"></div>

    <h1 class="headline">
      <span class="headline__lead">BENEFITS OF OUR</span>
      <span class="headline__service">WASH &amp; FOLD</span>
      <span class="headline__tail">SERVICE</span>
    </h1>

    <section class="benefits">
      <div class="benefit" style="left:31px;top:31px;">
        <svg viewBox="0 0 24 24"><circle cx="12" cy="12" r="11" fill="#f7941d"/><path d="M7 12.5l3.2 3.2L17 9" fill="none" stroke="#fff" stroke-width="2.6" stroke-linecap="round" stroke-linejoin="round"/></svg>
        SAVES MONEY
      </div>
      <div class="benefit" style="left:31px;top:67px;">
        <svg viewBox="0 0 24 24"><circle cx="12" cy="12" r="11" fill="#f7941d"/><path d="M7 12.5l3.2 3.2L17 9" fill="none" stroke="#fff" stroke-width="2.6" stroke-linecap="round" stroke-linejoin="round"/></svg>
        SAVES TIME
      </div>
      <div class="benefit" style="left:246px;top:31px;">
        <svg viewBox="0 0 24 24"><circle cx="12" cy="12" r="11" fill="#f7941d"/><path d="M7 12.5l3.2 3.2L17 9" fill="none" stroke="#fff" stroke-width="2.6" stroke-linecap="round" stroke-linejoin="round"/></svg>
        CONVENIENT
      </div>
      <div class="benefit" style="left:246px;top:67px;">
        <svg viewBox="0 0 24 24"><circle cx="12" cy="12" r="11" fill="#f7941d"/><path d="M7 12.5l3.2 3.2L17 9" fill="none" stroke="#fff" stroke-width="2.6" stroke-linecap="round" stroke-linejoin="round"/></svg>
        STAIN TREATMENT
      </div>
    </section>

    <div class="contact">
      <svg viewBox="0 0 24 24"><circle cx="12" cy="12" r="11" fill="#f7941d"/><path d="M8.6 6.5l1.8 2.6-1.1 1.4c.8 1.7 2 2.9 3.7 3.7l1.4-1.1 2.6 1.8-.9 2.2c-4.6.1-9.2-4.5-9.1-9.1z" fill="#fff"/></svg>
      <span class="contact__phone">555-014-2290</span>
      <span class="contact__divider">|</span>
      <svg viewBox="0 0 24 24"><circle cx="12" cy="12" r="11" fill="#f7941d"/><g fill="none" stroke="#fff" stroke-width="1.5"><circle cx="12" cy="12" r="6"/><ellipse cx="12" cy="12" rx="2.6" ry="6"/><path d="M6 12h12"/></g></svg>
      <span class="contact__web">www.<b>brightsudslaundry</b>.com</span>
    </div>
  </main>
</body>
</html>
```